Update Website, Include new Logo

We are a Technology Managed Service Provider (MSP)
+cyber security company operating out of New York City and New Jersey. Our main customer base has been financial service industry, high tech, multi-media, and/or other enterprise level customers. Current website is very old but still valid from an offering standpoint but we now want to emphasize and focus more on Cyber Security. We are offering a new cybersecurity line targeted at offering NGOs, Government, and Small-Mid Sized businesses the same level of cybersecurity as big business.

We would like to incorporate the new Pravlin logo and keep the feel modern, secure (without feeling aggressive). We want our clients to feel we will offer them white glove service at affordable cost - safety, security and stability are attainable at all levels.

I am attaching logos for visual, as you need copy, please let us know and we can send you the verbiage. Our current site is www.pravlin-example.com for comparison

Target Market(s)

Any businesses who need cyber security

Industry/Entity Type

Technology - Cybersecurity

Number of Pages Required

3 page

Colors
0054AA
0677BA
7BADD7
CADEEF
E8F1F8
FFC000
F8CF3A
FAE287
FDF2CF
FEFAEE
F0912C
F2A743
F7CA91
FBE8D2
FDF5EE
EE7325
F08F49
F5BC92
FAE3D3
FDF4ED

Requirements
Must have
• Bulleted points about SOC, compliance, Ambrolite, etc (see marketing doc). Please use the new Pravlin Logo (in zip), we like the orange version (with the fading color). Would like to have that color be included throughout, however do not want it to be childish. Open to ideas on colors/layout/imagery
Nice to have
• An area to capture customer data (schedule a Penetration Test, ask for more info, or check pricing), or a link/qr code area we can add that
Should not have
• Halloween feel, An aggressive feel, hard sell. Not large areas of paragraphs (like our current page).

```html
<!DOCTYPE html>
<html lang="en">
<head>
<meta charset="utf-8">
<title>Pravlin Technology</title>
<link href="https://fonts.googleapis.com/css2?family=Russo+One&family=Red+Hat+Display:wght@400;500;600;700&display=swap" rel="stylesheet">
<style>
:root{
  --orange:#f7760d;
  --orange-deep:#ee5a10;
  --amber:#ffb800;
  --yellow:#ffd300;
  --ink:#111111;
  --text:#555555;
  --muted:#6b6b6b;
  --field:#f1f1f1;
  --band:#f2f2f2;
  --white:#ffffff;
  --grad:linear-gradient(90deg,#ff6a00 0%,#ff9a00 55%,#ffc800 100%);
}
*{box-sizing:border-box;margin:0;padding:0}
html,body{width:1200px;height:3526px;overflow:hidden}
body{position:relative;background:var(--white);font-family:"Red Hat Display",Arial,sans-serif;color:var(--text)}
.abs{position:absolute}
.display{font-family:"Russo One","Arial Black",sans-serif;font-variant:small-caps;color:var(--ink);letter-spacing:.5px;font-weight:400}
.hex{clip-path:polygon(50% 0,100% 25%,100% 75%,50% 100%,0 75%,0 25%)}

/* header */
.site-header{position:absolute;left:0;top:0;width:1200px;height:93px;background:var(--white)}
.brand{position:absolute;display:flex;align-items:center;gap:10px}
.brand-mark{width:44px;height:44px;border-radius:50%;background:var(--grad)}
.brand-name{font-family:"Red Hat Display",sans-serif;font-weight:700;font-size:34px;color:var(--ink);line-height:1}
.brand-sub{font-size:11px;letter-spacing:3px;color:#9a9a9a;display:block;margin-top:2px}
.nav a{position:absolute;top:39px;font-size:12.5px;color:#333;text-decoration:none;font-weight:500}
.nav a.active::before{content:"";position:absolute;left:0;right:0;top:-39px;height:3px;background:var(--orange)}

/* buttons */
.btn{position:absolute;display:block;text-decoration:none}
.btn .frame{position:absolute;inset:0;width:100%;height:100%}
.btn .fill{position:absolute;left:10px;right:10px;top:4px;bottom:4px;background:var(--grad);
  clip-path:polygon(12px 0,calc(100% - 12px) 0,100% 50%,calc(100% - 12px) 100%,12px 100%,0 50%);
  color:#fff;font-weight:700;font-size:13px;display:flex;align-items:center;justify-content:center;letter-spacing:.3px}

/* hero */
.hero{position:absolute;left:0;top:93px;width:1200px;height:760px}
.hero-art{position:absolute;inset:0;background:radial-gradient(ellipse 55% 45% at 50% 70%,#c7420a 0%,#6e1a06 45%,#1a0603 75%,#000 100%)}
.hero h1{position:absolute;left:0;width:1200px;top:110px;text-align:center;color:#fff;font-size:54px;line-height:58px}
.hero h1 .accent{background:linear-gradient(90deg,#ff7a00,#ffc000);-webkit-background-clip:text;background-clip:text;color:transparent}
.hero .lede{position:absolute;left:0;width:1200px;top:240px;text-align:center;color:#fff;font-size:15px}
.down{position:absolute;left:566px;top:800px;width:68px;height:76px;background:#fff;display:flex;align-items:center;justify-content:center;filter:drop-shadow(0 4px 8px rgba(0,0,0,.15))}

/* intro */
.intro-mark{position:absolute;left:167px;top:923px;width:342px;height:393px;display:flex;align-items:center;justify-content:center}
.intro-mark .disc{width:330px;height:330px;border-radius:50%;background:linear-gradient(135deg,#ffe000 0%,#ffa000 50%,#ff5a00 100%)}
.intro h2{position:absolute;left:572px;top:980px;font-size:36px;line-height:44px}
.intro p{position:absolute;left:572px;top:1082px;width:462px;font-size:14.5px;line-height:22px}

/* services */
.section-title{position:absolute;left:0;width:1200px;text-align:center;font-size:38px;line-height:46px}
.service{position:absolute;top:1485px;width:220px;text-align:center}
.service .icon{width:124px;height:143px;margin:0 auto;background:#efefef;display:flex;align-items:center;justify-content:center}
.service h3{margin-top:22px;font-size:20px;color:var(--ink)}
.service p{margin-top:6px;font-size:13.5px;line-height:19px;color:var(--muted)}

/* white glove */
.band{position:absolute;left:0;top:1911px;width:1200px;height:587px;background:var(--band)}
.card{position:absolute;top:2089px;width:283px;height:327px;background:#fff;box-shadow:0 2px 10px rgba(0,0,0,.06)}
.card .photo{position:absolute;left:11px;top:11px;width:261px;height:226px}
.card .badge{position:absolute;left:107px;top:200px;width:68px;height:78px;background:#fff;display:flex;align-items:center;justify-content:center}
.card h3{position:absolute;left:0;width:100%;top:286px;text-align:center;font-size:20px;color:var(--ink)}

/* form */
.field{position:absolute;background:var(--field);font-size:13px;color:#777;padding:0 26px;display:flex;align-items:center}
.field.area{align-items:flex-start;padding-top:20px}

/* footer */
.footer-art{position:absolute;left:0;top:2990px;width:1200px;height:536px}
.footer h4{position:absolute;top:3176px;font-family:"Russo One",sans-serif;font-variant:small-caps;color:#fff;font-size:30px;font-weight:400}
.footer ul{position:absolute;list-style:none;top:3222px}
.footer li{color:#fff;font-size:13.5px;line-height:27px}
.contact-item{position:absolute;left:628px;color:#fff;font-size:13.5px;line-height:20px;padding-left:27px}
.contact-item svg{position:absolute;left:0;top:3px}
.social{position:absolute;top:3218px;width:46px;height:50px;background:#3a3a3a}
.social.first{background:var(--grad)}
.rule{position:absolute;left:89px;top:3454px;width:1022px;height:1px;background:#333}
.copy{position:absolute;left:0;width:1200px;top:3480px;text-align:center;color:#fff;font-size:13px}
.to-top{position:absolute;left:1126px;top:3424px;width:54px;height:60px;background:var(--grad);display:flex;align-items:center;justify-content:center}
</style>
</head>
<body>

<header class="site-header">
  <div class="brand" style="left:89px;top:22px">
    <span class="brand-mark"></span>
    <span><span class="brand-name">PRAVLIN</span><span class="brand-sub">TECHNOLOGY</span></span>
  </div>
  <nav class="nav">
    <a href="#" class="active" style="left:510px">HOME</a>
    <a href="#" style="left:588px">CYBERSECURITY</a>
    <a href="#" style="left:732px">MANAGED IT</a>
    <a href="#" style="left:851px">ABOUT US</a>
  </nav>
  <a class="btn" href="#" style="left:944px;top:24px;width:164px;height:46px">
    <svg class="frame" viewBox="0 0 164 46"><polyline points="14,2 2,23 14,44" fill="none" stroke="#222" stroke-width="1.5"/><polyline points="150,2 162,23 150,44" fill="none" stroke="#222" stroke-width="1.5"/></svg>
    <span class="fill">CONTACT US</span>
  </a>
</header>

<section class="hero">
  <div class="hero-art" role="img" aria-label="Dark digital network scene with a glowing orange padlock at its centre"></div>
  <svg class="abs" style="left:0;top:0" width="1200" height="760" viewBox="0 0 1200 760">
    <polygon points="0,612 600,744 1200,612 1200,760 0,760" fill="#fff"/>
    <polyline points="0,612 600,744 1200,612" fill="none" stroke="#ff9400" stroke-width="7"/>
  </svg>
  <h1 class="display">Enterprise Level <span class="accent">Cybersecurity</span><br>for Every Business.</h1>
  <p class="lede">Expert protection, personalized for NGOs, government, and small to mid-sized businesses.</p>
  <a class="btn" href="#" style="left:440px;top:282px;width:320px;height:46px">
    <svg class="frame" viewBox="0 0 320 46"><polyline points="14,2 2,23 14,44" fill="none" stroke="#fff" stroke-width="1.5"/><polyline points="306,2 318,23 306,44" fill="none" stroke="#fff" stroke-width="1.5"/></svg>
    <span class="fill">REQUEST A FREE CONSULTATION</span>
  </a>
</section>
<div class="down hex"><svg width="24" height="28" viewBox="0 0 24 28"><path d="M12 3v21M4 16l8 8 8-8" fill="none" stroke="#222" stroke-width="2"/></svg></div>

<section class="intro">
  <div class="intro-mark" role="img" aria-label="Pravlin brand emblem"><span class="disc"></span></div>
  <h2 class="display">Closing the Security<br>Gap for Mid Market.</h2>
  <p>In today's digital landscape, every organization, regardless of size, deserves robust protection. We bring the security standards of big business to your doorstep, with a service model that's both accessible and affordable.</p>
  <a class="btn" href="#" style="left:572px;top:1192px;width:166px;height:46px">
    <svg class="frame" viewBox="0 0 166 46"><polyline points="14,2 2,23 14,44" fill="none" stroke="#222" stroke-width="1.5"/><polyline points="152,2 164,23 152,44" fill="none" stroke="#222" stroke-width="1.5"/></svg>
    <span class="fill">LEARN MORE</span>
  </a>
</section>

<section class="services">
  <h2 class="section-title display" style="top:1418px">Our Service</h2>
  <div class="service" style="left:131px">
    <div class="icon hex"><svg width="64" height="64" viewBox="0 0 64 64" fill="none" stroke="#f7860d" stroke-width="2.5"><circle cx="32" cy="20" r="9"/><path d="M28 20l3 3 5-6"/><path d="M6 30v14l12 12h10M58 30v14L46 56H36"/></svg></div>
    <h3 class="display">Managed It</h3>
    <p>Many companies these days are realizing the benefits...</p>
  </div>
  <div class="service" style="left:370px">
    <div class="icon hex"><svg width="64" height="64" viewBox="0 0 64 64" fill="none" stroke="#f7860d" stroke-width="2.5"><rect x="6" y="26" width="20" height="16" rx="2"/><circle cx="34" cy="22" r="7"/><path d="M22 56c0-10 6-16 12-16s12 6 12 16"/><circle cx="50" cy="34" r="6"/></svg></div>
    <h3 class="display">Professional</h3>
    <p>Your technology needs to be as flexible as your business.</p>
  </div>
  <div class="service" style="left:608px">
    <div class="icon hex"><svg width="64" height="64" viewBox="0 0 64 64" fill="none" stroke="#f7860d" stroke-width="2.5"><path d="M16 34a10 10 0 0 1 2-20 14 14 0 0 1 27 2 9 9 0 0 1 3 18z"/><path d="M24 34v12M32 34v20M40 34v10"/><circle cx="44" cy="48" r="5"/></svg></div>
    <h3 class="display">Cloud Services</h3>
    <p>With the advent of Cloud Computing, it is now possible...</p>
  </div>
  <div class="service" style="left:848px">
    <div class="icon hex"><svg width="64" height="64" viewBox="0 0 64 64" fill="none" stroke="#f7860d" stroke-width="2.5"><path d="M24 30a10 10 0 1 1 16 0l-3 8H27z"/><path d="M27 44h10M29 50h6"/><rect x="42" y="8" width="16" height="10" rx="3"/><rect x="6" y="16" width="14" height="10" rx="3"/></svg></div>
    <h3 class="display">It Consulting</h3>
    <p>Pravlin Consulting Services will put you ahead of the curve...</p>
  </div>
  <a class="btn" href="#" style="left:517px;top:1772px;width:166px;height:46px">
    <svg class="frame" viewBox="0 0 166 46"><polyline points="14,2 2,23 14,44" fill="none" stroke="#222" stroke-width="1.5"/><polyline points="152,2 164,23 152,44" fill="none" stroke="#222" stroke-width="1.5"/></svg>
    <span class="fill">LEARN MORE</span>
  </a>
</section>

<section class="band" aria-hidden="false"></section>
<h2 class="section-title display" style="top:1973px">White-Glove Service Accessible<br>for All.</h2>
<article class="card" style="left:157px">
  <div class="photo" role="img" aria-label="Photo of a consultant in an orange shirt thinking in a bright office" style="background:linear-gradient(135deg,#5aa7a8 0%,#c9a98a 45%,#f08a1c 100%)"></div>
  <div class="badge hex"><svg width="34" height="34" viewBox="0 0 34 34" fill="none" stroke="#f7860d" stroke-width="2"><circle cx="14" cy="12" r="6"/><path d="M4 32c0-8 5-12 10-12s10 4 10 12"/><circle cx="27" cy="8" r="4"/></svg></div>
  <h3 class="display">Expert Guidance</h3>
</article>
<article class="card" style="left:458px">
  <div class="photo" role="img" aria-label="Glowing orange shield with a check mark on a brick wall" style="background:radial-gradient(circle at 50% 45%,#ff8a10 0%,#b33a08 40%,#2a0d05 85%)"></div>
  <div class="badge hex"><svg width="34" height="34" viewBox="0 0 34 34" fill="none" stroke="#f7860d" stroke-width="2"><circle cx="17" cy="17" r="6"/><path d="M17 3v5M17 26v5M3 17h5M26 17h5M7 7l4 4M23 23l4 4M27 7l-4 4M11 23l-4 4"/></svg></div>
  <h3 class="display">Proactive Protection</h3>
</article>
<article class="card" style="left:761px">
  <div class="photo" role="img" aria-label="Hands over a tablet with glowing orange price tags and charts" style="background:linear-gradient(160deg,#1c2550 0%,#3a4a9a 45%,#f07a20 100%)"></div>
  <div class="badge hex"><svg width="34" height="34" viewBox="0 0 34 34" fill="none" stroke="#f7860d" stroke-width="2"><path d="M4 30h26M8 30V20M14 30V14M20 30V18M26 30V8"/></svg></div>
  <h3 class="display">Predictable Pricing</h3>
</article>

<section class="contact-form">
  <h2 class="section-title display" style="top:2586px">Ready to Secure Your Future?</h2>
  <div class="field" style="left:171px;top:2658px;width:420px;height:52px">Enter Your Name...</div>
  <div class="field" style="left:171px;top:2724px;width:420px;height:52px">Enter Your Email...</div>
  <div class="field" style="left:171px;top:2791px;width:420px;height:52px">Enter Your Address...</div>
  <div class="field area" style="left:607px;top:2658px;width:422px;height:185px">Please Send Your Message...</div>
  <a class="btn" href="#" style="left:517px;top:2869px;width:166px;height:46px">
    <svg class="frame" viewBox="0 0 166 46"><polyline points="14,2 2,23 14,44" fill="none" stroke="#222" stroke-width="1.5"/><polyline points="152,2 164,23 152,44" fill="none" stroke="#222" stroke-width="1.5"/></svg>
    <span class="fill">LEARN MORE</span>
  </a>
</section>

<footer class="footer">
  <svg class="footer-art" viewBox="0 0 1200 536" width="1200" height="536">
    <polygon points="0,156 594,13 1200,156 1200,536 0,536" fill="#000"/>
    <polyline points="0,156 594,13 1200,156" fill="none" stroke="#ff9400" stroke-width="8"/>
  </svg>
  <div class="brand" style="left:92px;top:3252px">
    <span class="brand-mark"></span>
    <span><span class="brand-name" style="color:#fff">PRAVLIN</span><span class="brand-sub" style="color:#ccc">TECHNOLOGY</span></span>
  </div>
  <h4 style="left:373px">Quick Link</h4>
  <ul style="left:374px">
    <li>Home</li><li>Cybersecurity</li><li>Managed IT</li><li>About Us</li><li>Contact</li>
  </ul>
  <h4 style="left:628px">Contact Us</h4>
  <div class="contact-item" style="top:3224px"><svg width="13" height="13" viewBox="0 0 13 13"><path d="M3 1l2 3-1.5 1.5a7 7 0 0 0 4 4L9 8l3 2-1 2C6 12 1 7 1 2z" fill="#f7860d"/></svg>Phone:<br>(555) 014-2290</div>
  <div class="contact-item" style="top:3272px"><svg width="13" height="13" viewBox="0 0 13 13"><rect x="0.5" y="2.5" width="12" height="8" fill="#f7860d"/><path d="M1 3l5.5 4L12 3" fill="none" stroke="#000" stroke-width="1"/></svg>Email:<br>info@pravlin-example.com</div>
  <div class="contact-item" style="top:3320px"><svg width="13" height="13" viewBox="0 0 13 13"><path d="M6.5 12S2 7.5 2 5a4.5 4.5 0 0 1 9 0c0 2.5-4.5 7-4.5 7z" fill="#f7860d"/><circle cx="6.5" cy="5" r="1.6" fill="#000"/></svg>Address:<br>48 Harbor Row, New York, NY<br>210 Ridge Lane, Jersey City, NJ</div>
  <h4 style="left:925px">Follow Us</h4>
  <span class="social hex first" style="left:924px" role="img" aria-label="Social profile link"></span>
  <span class="social hex" style="left:970px" role="img" aria-label="Social profile link"></span>
  <span class="social hex" style="left:1017px" role="img" aria-label="Social profile link"></span>
  <span class="social hex" style="left:1063px" role="img" aria-label="Social profile link"></span>
  <div class="rule"></div>
  <p class="copy">© 2025 Pravlin. All rights reserved.</p>
  <div class="to-top hex"><svg width="20" height="24" viewBox="0 0 20 24"><path d="M10 22V3M3 10l7-7 7 7" fill="none" stroke="#fff" stroke-width="2"/></svg></div>
</footer>

</body>
</html>
```